Quillmere Voyage Care Web Page

To create a web page that has the number 1 goal of converting Zorvix Ad / Trellisgram Ads clicks into paying customers.
The site will feed into a web application where travellers can enter their trip and purchase a Voyawell Ready Pack.
The page / site needs to be able to tell people what we do and encourage them to start the process of getting a Voyawell Ready Pack.
It should be a wordpress theme.
Please see the attached brief for more information.

```html
<!DOCTYPE html>
<html lang="en">
<head>
<meta charset="utf-8">
<title>Quillmere Voyage Care</title>
<link rel="stylesheet" href="https://fonts.googleapis.com/css2?family=Poppins:wght@300;400;500;600&family=Lora:wght@500&display=swap">
<style>
:root{
  --ink:#17171f;
  --navy:#2d4a73;
  --blue:#4f8db4;
  --muted:#5e5e6a;
  --hero-a:#eeeafc;
  --hero-b:#f8eafb;
  --soft-circle:#e4e0f7;
  --white:#ffffff;
}
*{box-sizing:border-box;margin:0;padding:0}
html,body{width:998px;height:1200px;overflow:hidden;background:var(--white)}
body{position:relative;font-family:"Poppins",sans-serif;color:var(--ink)}
.abs{position:absolute}

.hero{position:absolute;left:0;top:0;width:998px;height:496px;background:linear-gradient(100deg,var(--hero-a),var(--hero-b))}
.brand{left:114px;top:34px;display:flex;align-items:center;gap:8px}
.brand-dot{width:24px;height:24px;border-radius:50%;background:var(--blue)}
.brand-name{font-size:14px;font-weight:600;color:var(--navy)}
.nav{top:15px;font-family:"Lora",serif;font-size:9.5px;font-weight:500;color:#222}
.hire{left:789px;top:7px;width:78px;height:26px;border:1px solid #222;border-radius:13px;font-family:"Lora",serif;font-size:9.5px;display:flex;align-items:center;justify-content:center}

.hero-title{left:114px;top:116px;font-size:36px;font-weight:600;line-height:41px;color:var(--ink)}
.hero-title span{color:var(--blue)}
.hero-lead{left:114px;top:203px;width:340px;font-size:10.3px;line-height:17.3px;color:#3a3a44;font-weight:300}

.search{left:114px;top:267px;width:272px;height:30px;background:var(--white);border:1px solid #e1dfe8;border-radius:3px;font-size:9px;color:#a3a3ad;font-weight:300}
.search .field{position:absolute;left:9px;top:9px}
.search .divider{position:absolute;left:147px;top:0;width:1px;height:100%;background:#e1dfe8}
.search .cat{position:absolute;left:156px;top:9px}
.search svg{position:absolute;right:12px;top:11px}
.search-btn{left:396px;top:267px;width:31px;height:30px;background:var(--blue);border-radius:3px;display:flex;align-items:center;justify-content:center}

.avatars{left:114px;top:382px;display:flex}
.avatars i{width:29px;height:29px;border-radius:50%;border:2px solid var(--white);margin-right:-8px}
.social-proof{left:195px;top:392px;font-size:8px;color:#444}
.social-proof b{font-weight:500;color:var(--navy)}

.circle{border-radius:50%}
.deco{background:var(--soft-circle)}

.who{left:114px;top:572px;font-size:11px;font-weight:600;letter-spacing:2.2px;color:var(--navy)}
.who-title{left:114px;top:588px;font-size:34px;font-weight:600;line-height:39px}
.who-copy{left:114px;top:692px;width:390px;font-size:10.2px;line-height:17.3px;color:var(--muted)}
.stat{top:783px;width:109px;height:83px;background:var(--white);border-radius:6px;box-shadow:0 6px 18px rgba(60,60,110,.07);text-align:center}
.stat strong{display:block;margin-top:14px;font-size:24px;font-weight:500;color:var(--navy);line-height:30px}
.stat span{display:block;margin-top:5px;font-size:10.3px;color:var(--muted)}
.team-photo{left:529px;top:570px;width:344px;height:289px;border-radius:7px;background:linear-gradient(135deg,#d9d9d9,#8e8e8e 55%,#3a3a3a)}

.cta{left:50px;top:915px;width:898px;height:285px;border-radius:4px 4px 0 0;overflow:hidden;background:linear-gradient(90deg,#4e98c1 0%,#7a6ee6 35%,#8a5bf0 52%,#5b55c4 75%,#37507f 100%)}
.cta-kicker{position:absolute;left:0;right:0;top:68px;text-align:center;font-size:17px;font-weight:300;color:rgba(255,255,255,.85)}
.cta-mail{position:absolute;left:0;right:0;top:105px;text-align:center;font-size:28px;font-weight:600;color:var(--white);text-decoration:underline;text-underline-offset:4px;text-decoration-thickness:2px}
.cta-btn{position:absolute;left:398px;top:173px;width:103px;height:36px;background:var(--white);border-radius:3px;font-size:11.5px;color:var(--ink);display:flex;align-items:center;justify-content:center}
</style>
</head>
<body>
<section class="hero">
  <div class="abs brand"><span class="brand-dot"></span><span class="brand-name">Quillmere Voyage Care</span></div>
  <a class="abs nav" style="left:474px">Home</a>
  <a class="abs nav" style="left:529px">About me</a>
  <a class="abs nav" style="left:599px">My Blog</a>
  <a class="abs nav" style="left:663px">Services</a>
  <a class="abs nav" style="left:728px">Contact</a>
  <a class="abs hire">Hire me</a>

  <h1 class="abs hero-title">Travel <span>Health</span><br>with No Limits</h1>
  <p class="abs hero-lead">Enjoy our great selection of travels. Choose from more than 25K<br>online video travel and become an health expert now!</p>

  <div class="abs search">
    <span class="field">Search travel...</span>
    <span class="divider"></span>
    <span class="cat">Categories</span>
    <svg width="8" height="6" viewBox="0 0 8 6"><path d="M1 1l3 3 3-3" fill="none" stroke="#333" stroke-width="1.3"/></svg>
  </div>
  <div class="abs search-btn">
    <svg width="12" height="12" viewBox="0 0 12 12"><circle cx="5" cy="5" r="3.8" fill="none" stroke="#fff" stroke-width="1.3"/><path d="M8 8l3 3" stroke="#fff" stroke-width="1.3"/></svg>
  </div>

  <div class="abs avatars">
    <i role="img" aria-label="Traveller portrait" style="background:#f2b54a"></i>
    <i role="img" aria-label="Traveller portrait" style="background:#5fb6e0"></i>
    <i role="img" aria-label="Traveller portrait" style="background:#8fd46a"></i>
  </div>
  <p class="abs social-proof"><b>10K+ traveller</b> are already with us</p>

  <div class="abs circle deco" style="left:686px;top:47px;width:84px;height:84px;background:#e6dcf8"></div>
  <div class="abs circle deco" style="left:536px;top:270px;width:118px;height:118px"></div>
  <div class="abs circle" role="img" aria-label="Smiling traveller portrait" style="left:509px;top:79px;width:94px;height:94px;background:radial-gradient(circle,#f7e06a,#eec426);border:2px solid #fff"></div>
  <div class="abs circle" role="img" aria-label="Student traveller with notebook" style="left:722px;top:43px;width:164px;height:164px;background:radial-gradient(circle,#7fcf82,#4fae57);border:2px solid #fff"></div>
  <div class="abs circle" role="img" aria-label="Health advisor with laptop" style="left:576px;top:133px;width:212px;height:212px;background:radial-gradient(circle,#ececec,#d6d6d6);border:3px solid #fff;box-shadow:0 10px 30px rgba(120,110,170,.18)"></div>
  <div class="abs circle" role="img" aria-label="Traveller in casual shirt" style="left:717px;top:305px;width:128px;height:128px;background:radial-gradient(circle,#f3c9a2,#e9a46f);border:2px solid #fff"></div>
</section>

<p class="abs who">WHO WE ARE</p>
<h2 class="abs who-title">Building Trips for<br>Amazing changers</h2>
<p class="abs who-copy">Lorem ipsum dolor sit amet, consectetur adipiscing elit. Suspendisse nec turpis mi. Sed varius ligula at lorem finibus molestie. Pellentesque vel orci et ligula egestas dapibus. Sed quis orci eget lorem porttitor fermentum quis vitae lacus.</p>
<div class="abs stat" style="left:114px"><strong>12+</strong><span>Experience</span></div>
<div class="abs stat" style="left:244px"><strong>105+</strong><span>Projects</span></div>
<div class="abs stat" style="left:374px"><strong>100%</strong><span>Client Happy</span></div>
<div class="abs team-photo" role="img" aria-label="Team working on laptops at a table, black and white"></div>

<section class="abs cta">
  <p class="cta-kicker">Want to work with us? Let’s talk</p>
  <p class="cta-mail">hello@quillmere-mail.com</p>
  <a class="cta-btn">Contact us</a>
</section>
</body>
</html>
```